Wine label for boutique family-owned winery

We need a front wine label designed for Mirelo, our small, family-owned, Oregon based winery . Mirelo makes warm climate red blends with grapes sourced from SE Washington state, USA. We are a startup business with wines for 2013 and 2014.

The name Mirelo comes from the Georgian language, and is short for Cornelius, my father's name. The Georgians have an 5000-8000 year history of winemaking, out of which they give heartfelt toasts that celebrate kinship, family, and loved ones of the past and future.

The design can be of various aspect ratios, but should fit flatly on a bordeaux style wine bottle.
We would like this wine label to work for red wines, and be convertible to work with white wines with some simple background color changes. The preferred file format is Adobe Illustrator. This label will be digitally printed.

A couple wine labels that I like:
- 9 Lanterns
- pikrastudio.com/labels "fern"

I am including a file to show what the existing Mirelo label looks like.
Updates

Reason: To give more time for designer revisions. We want the right design!

Target Market(s)

Direct sales through group tastings.
Professionals aged 30-65 with disposable income.
$35/bottle wine.

Industry/Entity Type

Boutique

Font styles to use
Serif
Decorative
Script

Requirements
Must have
• Rich and/or earthy tones (see link to "Fern" above)
• The text on the front label will include:
• The brand name- Mirelo
• Vintage: 2013
• Wine name- Marigold Blend
• AVA: Washington State
• (The specific information will vary, but we need room for those categories of text.)
Nice to have
• We'd like to convey the qualities of sincerity, trustworthiness, and being grounded. If it's possible to convey our philosophy of sharing wine with friends and family that would be great.
• We have an existing logo "Mirelo" that has been attached as an SVG file.
• It is not required to include this logo, but if it works in your design, all the better.
Should not have
• Feature photographs or likenesses of photographs

```html
<!DOCTYPE html>
<html lang="en">
<head>
<meta charset="utf-8">
<title>Mirelo – Marigold Blend Front Labels</title>
<link rel="stylesheet" href="https://fonts.googleapis.com/css2?family=Cinzel:wght@400;600&display=swap">
<style>
  :root {
    --backdrop-top: #cfcfd1;
    --backdrop-bottom: #f4f4f5;
    --label-black: #050505;
    --silver-light: #f1f1f2;
    --silver-mid: #cfd0d2;
    --silver-dark: #a9aaad;
    --gold: #b8953f;
    --gold-light: #d8bd6e;
    --brand-red: #9e1b2c;
    --ink-dark: #1c1c1c;
    --ink-light: #efefef;
    --lake-blue: #2d6fb3;
    --sunset-orange: #e9a23b;
    --harbour-red: #b84a4a;
    --harbour-blue: #3a7fc4;
  }

  * { box-sizing: border-box; margin: 0; padding: 0; }

  html, body {
    width: 800px;
    height: 1200px;
    overflow: hidden;
  }

  body {
    background: linear-gradient(to bottom, var(--backdrop-top), var(--backdrop-bottom));
    font-family: "Cinzel", serif;
    display: flex;
    align-items: center;
    justify-content: center;
    gap: 40px;
  }

  .label {
    width: 360px;
    height: 480px;
    display: flex;
    flex-direction: column;
    box-shadow: 0 6px 18px rgba(0, 0, 0, 0.18);
  }

  .silver-panel {
    background: linear-gradient(to bottom, var(--silver-dark), var(--silver-light) 35%, var(--silver-mid) 70%, var(--silver-light));
  }

  .artwork-lake {
    height: 150px;
    background:
      linear-gradient(to bottom,
        #2f5f9e 0%, #e6a53c 22%, #3a68a8 34%, #f0b451 46%,
        #1f4f86 54%, #e9b45a 64%, #4d86bf 76%, #f2c77c 88%, #3f77b1 100%);
  }

  .artwork-harbour {
    height: 150px;
    background:
      linear-gradient(to right,
        #c9583f 0%, #3b6fb4 18%, #e4a24a 34%, #b8434c 48%,
        #4a8fd0 62%, #e8b155 78%, #2f66a8 90%, #d88a3c 100%);
    border-bottom: 4px solid var(--brand-red);
  }

  .badge-band {
    height: 150px;
    background: var(--label-black);
    border-top: 4px solid var(--gold);
    border-bottom: 4px solid var(--gold);
    display: flex;
    align-items: center;
    justify-content: center;
  }

  .badge {
    width: 136px;
    height: 136px;
    border-radius: 50%;
    background: radial-gradient(circle at 40% 35%, var(--gold-light), var(--gold));
    display: flex;
    align-items: center;
    justify-content: center;
    font-size: 22px;
    font-weight: 600;
    color: var(--label-black);
    letter-spacing: 0.04em;
  }

  .brand-strip {
    height: 132px;
    display: flex;
    align-items: center;
    justify-content: center;
    font-size: 34px;
    font-weight: 600;
    color: var(--label-black);
    letter-spacing: 0.06em;
  }

  .details {
    flex: 1;
    display: flex;
    flex-direction: column;
    align-items: center;
    justify-content: center;
    text-align: center;
  }

  .details--silver { color: var(--ink-dark); }
  .details--black { background: var(--label-black); color: var(--ink-light); }

  .brand-name {
    font-size: 24px;
    font-weight: 400;
    color: var(--brand-red);
    letter-spacing: 0.03em;
    margin-bottom: 10px;
  }

  .wine-name {
    font-size: 23px;
    font-weight: 400;
    letter-spacing: 0.06em;
    margin-bottom: 12px;
  }

  .vintage {
    font-size: 15px;
    letter-spacing: 0.3em;
    margin-bottom: 20px;
  }

  .ava {
    font-size: 11px;
    letter-spacing: 0.1em;
  }
</style>
</head>
<body>

  <section class="label label--lake">
    <div class="artwork-lake" role="img" aria-label="Painted sunset over a lake with distant blue mountains"></div>
    <div class="badge-band">
      <div class="badge">Mirelo</div>
    </div>
    <div class="details details--silver silver-panel">
      <p class="brand-name">Mirelo</p>
      <h1 class="wine-name">Marigold Blend</h1>
      <p class="vintage">2013</p>
      <p class="ava">Washington State</p>
    </div>
  </section>

  <section class="label label--harbour">
    <div class="brand-strip silver-panel">Mirelo</div>
    <div class="artwork-harbour" role="img" aria-label="Painted blue boat resting on water with colourful reflections"></div>
    <div class="details details--black">
      <p class="brand-name">Mirelo</p>
      <h1 class="wine-name">Marigold Blend</h1>
      <p class="vintage">2013</p>
      <p class="ava">Washington State</p>
    </div>
  </section>

</body>
</html>
```